Drovane Supplies Ltd Stationery Design Project

hi we need to design business cards, letter head, complimentary slips, scribble pads, note pads, envelopes for drovane supplies ltd.

please see business cards details

Kelwin Osterby

P.O Box 43817 -00291 Nairobi - Kenya
Tel: +254-733-281-914
Email: drovanesupplies@mailvaro.example

company name should appear on all stationery : Drovane Supplies Ltd

Industry/Entity Type

Business

Requirements
Must have
• kindly stick to colours in the logo

```html
<!DOCTYPE html>
<html lang="en">
<head>
<meta charset="utf-8">
<title>Drovane Supplies Ltd – Business Card</title>
<link rel="stylesheet" href="https://fonts.googleapis.com/css2?family=Bree+Serif&display=swap">
<style>
  :root {
    --page-bg: #dcd9d3;
    --card-bg: #ffffff;
    --ink: #3d3d3f;
    --brand-orange: #f39320;
    --brand-navy: #25308a;
    --ornament-light: #e6e6e6;
    --ornament-fade: rgba(255, 255, 255, 0);
  }
  * { margin: 0; padding: 0; box-sizing: border-box; }
  html, body {
    width: 1200px;
    height: 938px;
    overflow: hidden;
    background: var(--page-bg);
  }
  .canvas {
    position: relative;
    width: 1200px;
    height: 938px;
  }
  .card-back {
    position: absolute;
    left: 161px;
    top: 153px;
    width: 955px;
    height: 573px;
    background: var(--brand-orange);
  }
  .business-card {
    position: absolute;
    left: 84px;
    top: 207px;
    width: 962px;
    height: 576px;
    background: var(--card-bg);
    font-family: "Bree Serif", Georgia, serif;
    color: var(--ink);
    overflow: hidden;
  }
  .card-ornament {
    position: absolute;
    left: 685px;
    top: 19px;
    width: 560px;
    height: 560px;
    border-radius: 50%;
    background: radial-gradient(circle at 50% 50%,
      var(--card-bg) 0%, var(--card-bg) 30%,
      var(--ornament-light) 36%, var(--ornament-light) 62%,
      var(--ornament-fade) 100%);
  }
  .holder-name {
    position: absolute;
    left: 60px;
    top: 50px;
    font-size: 44px;
    line-height: 1;
    font-weight: 400;
  }
  .holder-email {
    position: absolute;
    left: 63px;
    top: 101px;
    display: flex;
    align-items: center;
    gap: 10px;
    font-size: 21px;
    line-height: 26px;
  }
  .holder-email svg { width: 24px; height: 17px; }
  .brand-block {
    position: absolute;
    left: 480px;
    top: 248px;
    transform: translate(-50%, -50%);
    display: flex;
    align-items: center;
    gap: 14px;
    white-space: nowrap;
  }
  .brand-mark {
    width: 40px;
    height: 40px;
    border-radius: 50%;
    background: var(--brand-orange);
  }
  .brand-name {
    font-size: 40px;
    line-height: 1;
    color: var(--brand-navy);
    font-weight: 400;
  }
  .contact-block {
    position: absolute;
    left: 308px;
    top: 466px;
    font-size: 21px;
    line-height: 29px;
  }
  .contact-line { display: flex; align-items: center; gap: 8px; }
  .contact-line svg { width: 20px; height: 24px; }
</style>
</head>
<body>
<div class="canvas">
  <div class="card-back"></div>
  <div class="business-card">
    <div class="card-ornament" role="img" aria-label="Faint grey swirling sun ornament along the right edge"></div>

    <h1 class="holder-name">Kelwin Osterby</h1>
    <p class="holder-email">
      <svg viewBox="0 0 24 17" aria-hidden="true">
        <rect x="0" y="0" width="24" height="17" fill="var(--brand-orange)"/>
        <polyline points="1,1 12,10 23,1" fill="none" stroke="#ffffff" stroke-width="2"/>
      </svg>
      drovanesupplies@mailvaro.example
    </p>

    <div class="brand-block">
      <span class="brand-mark" aria-hidden="true"></span>
      <span class="brand-name">Drovane Supplies</span>
    </div>

    <div class="contact-block">
      <p class="contact-line">P.O Box 43817 -00291 Nairobi - Kenya</p>
      <p class="contact-line">
        <svg viewBox="0 0 20 24" aria-hidden="true">
          <rect x="1" y="1" width="18" height="22" rx="2" fill="none" stroke="var(--ink)" stroke-width="2"/>
          <rect x="4" y="3" width="4" height="18" fill="var(--ink)"/>
          <rect x="11" y="5" width="5" height="4" fill="var(--ink)"/>
          <rect x="11" y="12" width="5" height="2" fill="var(--ink)"/>
          <rect x="11" y="16" width="5" height="2" fill="var(--ink)"/>
        </svg>
        +254-733-281-914
      </p>
    </div>
  </div>
</div>
</body>
</html>
```